Website and Mobile Devices design for food related application.

We need a design that is simple yet playful. The design should be food related if possible.
This design will be on the website and the mobile platform markets we intend application to be deployed too.
This application/website is called "Pickvoro[.com]. Its a random restaurant picker for the indecisive users.
Updates
Hi all, I picked a design. Again lots of great designs were submitted but I picked one that was more in line with what I wanted.
Target Market(s)
young internet savvy users.
Industry/Entity Type
Restaurant
Look and feel
Each slider illustrates characteristics of the customer's brand and the style your logo design should communicate.

```html
<!DOCTYPE html>
<html lang="en">
<head>
<meta charset="utf-8">
<title>Pickvoro</title>
<link rel="stylesheet" href="https://fonts.googleapis.com/css2?family=Aleo:ital,wght@0,300;0,700;1,700&display=swap">
<style>
  :root {
    --page-bg: #fbf1cd;
    --header-orange: #f26633;
    --header-band: #e5413b;
    --ink: #2a2622;
    --white: #ffffff;
    --rim: #e4ddc9;
    --rim-edge: #d9d1bb;
    --seg-blue: #3e6a8a;
    --seg-teal: #3aa596;
    --seg-green: #42ac4e;
    --seg-yellow: #e5c90b;
    --seg-orange: #f2b035;
    --seg-red: #ce3246;
    --spin-orange: #ee6130;
    --icon-tint: rgba(255, 255, 255, 0.45);
  }
  * { box-sizing: border-box; margin: 0; padding: 0; }
  html, body {
    width: 1200px;
    height: 986px;
    overflow: hidden;
    background: var(--page-bg);
    font-family: "Aleo", Georgia, serif;
    color: var(--ink);
  }
  .site-header {
    height: 100px;
    background: var(--header-orange);
    border-bottom: 12px solid var(--header-band);
    height: 112px;
    display: flex;
    align-items: center;
    justify-content: space-between;
    padding: 0 82px 12px 63px;
  }
  .brand-name {
    font-weight: 700;
    font-size: 43px;
    color: var(--white);
    letter-spacing: 0.3px;
  }
  .nav-link {
    font-weight: 300;
    font-size: 23px;
    color: var(--white);
    text-decoration: underline;
    text-underline-offset: 4px;
    text-decoration-thickness: 1px;
  }
  .picker {
    display: flex;
    flex-direction: column;
    align-items: center;
  }
  .picker-prompt {
    margin-top: 64px;
    font-weight: 300;
    font-size: 30px;
    letter-spacing: 0.2px;
  }
  .picker-wheel {
    margin-top: 28px;
    width: 560px;
    height: 560px;
  }
  .spin-label {
    font-family: "Aleo", Georgia, serif;
    font-weight: 700;
    font-style: italic;
    font-size: 22px;
    fill: var(--white);
  }
</style>
</head>
<body>
  <header class="site-header">
    <div class="brand-name">Pickvoro</div>
    <a class="nav-link" href="#">Contacts</a>
  </header>

  <main class="picker">
    <h1 class="picker-prompt">Today I’m feeling....</h1>

    <svg class="picker-wheel" viewBox="-240 -240 480 480" aria-label="Cuisine wheel">
      <circle class="wheel-rim" r="238" fill="var(--rim)" stroke="var(--rim-edge)" stroke-width="2"/>

      <path class="segment segment-teal" d="M0 0 L109 -188.8 A218 218 0 0 1 218 0 Z" fill="var(--seg-teal)"/>
      <path class="segment segment-green" d="M0 0 L218 0 A218 218 0 0 1 109 188.8 Z" fill="var(--seg-green)"/>
      <path class="segment segment-yellow" d="M0 0 L109 188.8 A218 218 0 0 1 -109 188.8 Z" fill="var(--seg-yellow)"/>
      <path class="segment segment-orange" d="M0 0 L-109 188.8 A218 218 0 0 1 -218 0 Z" fill="var(--seg-orange)"/>
      <path class="segment segment-red" d="M0 0 L-218 0 A218 218 0 0 1 -109 -188.8 Z" fill="var(--seg-red)"/>

      <path class="segment-highlight" d="M0 0 L-123 -196.7 A232 232 0 0 1 123 -196.7 Z" fill="#f7f5ef"/>
      <path class="segment segment-blue" d="M0 -14 L-104 -184 A214 214 0 0 1 104 -184 Z" fill="var(--seg-blue)"/>

      <g class="segment-icons" fill="var(--icon-tint)">
        <circle cx="0" cy="-140" r="38" role="img" aria-label="Noodle bowl icon"/>
        <circle cx="121" cy="-70" r="38" role="img" aria-label="Burger icon"/>
        <circle cx="121" cy="70" r="38" role="img" aria-label="Sushi roll icon"/>
        <circle cx="0" cy="140" r="38" role="img" aria-label="Cupcake icon"/>
        <circle cx="-121" cy="70" r="38" role="img" aria-label="Pizza icon"/>
        <circle cx="-121" cy="-70" r="38" role="img" aria-label="Beer mug icon"/>
      </g>

      <circle class="spin-ring" r="48" fill="var(--white)"/>
      <circle class="spin-button" r="40" fill="var(--spin-orange)"/>
      <text class="spin-label" x="0" y="8" text-anchor="middle">Spin!</text>
    </svg>
  </main>
</body>
</html>
```